Interior Design/ decoration business card design

This card is for my Interior Design and Decoration business and later I will also be selling homewares. I would like the card to be very simple in design and like either white, duck egg blue , aquas or metallics on a flat mat card excellent quality card. It needs to be well designed as that is my field. I dont like fuss, the simpler the better. I would like a styalised wren under the name wren if possible. SIMPLE, STYLISH, CLASSIC, TASTEFUL

Target Market(s)

40 + year olds who are building or rennovating.

Industry/Entity Type

Business

Contact Information for Business Card

Wren
styling, design, homeware

Maren Tulloch
p 0437165093
e maren@wrenliving.com.au
w wrenliving.com.au

Requirements
Must have
• very simple, stylish, classic, sophisticated. Simple and easy to read text that is a print similar to attached image. I like simple round A's though not as in attached image.

Double sided. It wont save as double sided for some reason!!
Should not have
• not too much colour, No animated / cartoon pictures.

```html
<!DOCTYPE html>
<html lang="en">
<head>
<meta charset="utf-8">
<title>Wren business card</title>
<link rel="stylesheet" href="https://fonts.googleapis.com/css2?family=Arimo:wght@400;700&family=Dancing+Script:wght@400;500&display=swap">
<style>
  :root {
    --duck-egg: #a9dcd7;
    --teal: #7ba39d;
    --paper: #ffffff;
  }
  html, body {
    margin: 0;
    padding: 0;
    width: 1200px;
    height: 781px;
    overflow: hidden;
    background: var(--duck-egg);
  }
  .canvas {
    position: relative;
    width: 1200px;
    height: 781px;
  }
  .card {
    position: absolute;
    box-sizing: border-box;
    box-shadow: 0 4px 10px rgba(40, 90, 85, 0.25);
  }
  .card-front {
    left: 134px; top: 22px; width: 378px; height: 656px;
    background: var(--teal);
    border: 10px solid var(--paper);
    color: var(--paper);
  }
  .card-back {
    left: 655px; top: 79px; width: 377px; height: 651px;
    background: var(--paper);
    border: 9px solid var(--teal);
    color: var(--teal);
  }
  .brand {
    position: absolute;
    left: 0; right: 0;
    margin: 0;
    text-align: center;
    font-family: "Dancing Script", cursive;
    font-weight: 400;
    line-height: 1;
  }
  .card-front .brand { top: 134px; font-size: 66px; }
  .card-back .brand { top: 60px; font-size: 44px; }
  .services {
    position: absolute;
    left: 0; right: 0;
    margin: 0; padding: 0;
    list-style: none;
    font-family: "Dancing Script", cursive;
    font-weight: 400;
  }
  .services li {
    display: flex;
    align-items: center;
    justify-content: center;
  }
  .services .dot {
    display: block;
    border-radius: 50%;
    background: currentColor;
  }
  .card-front .services { top: 304px; font-size: 42px; }
  .card-front .services li { height: 48.5px; }
  .card-front .services .dot { width: 14px; height: 14px; }
  .card-back .services { top: 131px; font-size: 31px; }
  .card-back .services li { height: 31px; }
  .card-back .services .dot { width: 8px; height: 8px; }
  .holder {
    position: absolute;
    left: 20px; right: 0; top: 336px;
    margin: 0;
    text-align: center;
    font-family: "Dancing Script", cursive;
    font-weight: 500;
    font-size: 52px;
    line-height: 1;
  }
  .contact {
    position: absolute;
    font-family: "Arimo", sans-serif;
    font-weight: 700;
    font-size: 23px;
    line-height: 1;
    text-align: right;
    white-space: nowrap;
  }
  .contact-phone { top: 460px; right: 23px; }
  .contact-email { top: 520px; right: 30px; }
  .contact-web { top: 578px; right: 29px; }
</style>
</head>
<body>
<main class="canvas">
  <section class="card card-front" aria-label="Card front">
    <p class="brand">Wren</p>
    <ul class="services">
      <li>styling</li>
      <li><span class="dot"></span></li>
      <li>design</li>
      <li><span class="dot"></span></li>
      <li>homeware</li>
    </ul>
  </section>

  <section class="card card-back" aria-label="Card back">
    <p class="brand">Wren</p>
    <ul class="services">
      <li>styling</li>
      <li><span class="dot"></span></li>
      <li>design</li>
      <li><span class="dot"></span></li>
      <li>homeware</li>
    </ul>
    <p class="holder">Maren Tulloch</p>
    <div class="contact contact-phone">043 716 5093</div>
    <div class="contact contact-email">maren@wrenliving.com.au</div>
    <div class="contact contact-web">www.wrenliving.com.au</div>
  </section>
</main>
</body>
</html>
```